Boutique Fitness Center needs a front window / door wrap

We need a front door and window wrap for our new fitness location called VolaRenx. We are a higher end, boutique body transformation center that will be opening soon.

We are looking to have 2 medium windows and 2 glass doors that are in the front of the facility wrapped - drawing attention to our facility in a bold, but classy way.

Our colors are Black, Yellow, Gray and White

There should be some artistic elements to the design.

I have attached a photo of our building. We are having a large 15' x 5' sign hung above the awning with our logo (logo also attached for reference)

The measurements for the 2 doors and 2 windows are as follows:
Both Doors: 30. 75" wide x 70.5" High
Both Windows: 73" wide x 59" High

Our ideas for the two doors are that on door one (door to left of picture) have the word "CONFIDENCE" in yellow written vertically with a light ghost image in the background of someone working out, possibly doing push-ups or battle ropes.

And on door #2 (door to the right of the picture) have the word "ESTEEM" written vertically in yellow with some type of light ghost image in the background

I have attached an example photo of where I got the idea of having large bold letters vertically written on the doors.

On the two large windows to the far left and right, I'd like to have a workout image of a female on one window and a male on the other doing a movement such slam balls, battle ropes, push-ups, etc. (No big bodybuilders, no image of traditional workout machines)

The window images should be done in black, white and gray colors.

I have attached an example image of a gym in New York, 82K, that I really like how the image is black and white with a pop of yellow.

On the Far Right window I would also like to have the text "Change Begins Here" with maybe an curved arrow pointing to the door.
The text should be distressed looking, similar to our logo and this is where pops of yellow can be added.

Use the example photos I've attached as reference and I'm excited to see what you're able to come up with.

```html
<!DOCTYPE html>
<html lang="en">
<head>
<meta charset="utf-8">
<title>VolaRenx — Window Wrap</title>
<link rel="stylesheet" href="https://fonts.googleapis.com/css2?family=Anton&family=Montserrat:wght@700&display=swap">
<style>
  :root {
    --paper: #ffffff;
    --ink: #000000;
    --night: #080808;
    --yellow: #f6d015;
    --white: #ffffff;
    --photo-light: #6e6e6e;
    --photo-mid: #3a3a3a;
    --photo-dark: #121212;
  }
  html, body {
    margin: 0;
    padding: 0;
    width: 1200px;
    height: 1200px;
    overflow: hidden;
    background: var(--paper);
  }
  .canvas {
    position: relative;
    width: 1200px;
    height: 1200px;
    background: var(--paper);
  }
  .wrap-band {
    position: absolute;
    left: 0;
    top: 115px;
    width: 1200px;
    height: 969px;
    background: var(--night);
    overflow: hidden;
  }
  .athlete-photo {
    position: absolute;
    left: 0;
    top: 0;
    width: 637px;
    height: 969px;
    background:
      radial-gradient(ellipse 40% 45% at 55% 40%, var(--photo-light) 0%, transparent 70%),
      linear-gradient(90deg, var(--photo-mid) 0%, var(--photo-dark) 100%);
  }
  .artwork {
    position: absolute;
    left: 0;
    top: 0;
    width: 1200px;
    height: 969px;
  }
  .brand-name {
    font-family: "Anton", sans-serif;
    fill: var(--white);
  }
  .tagline {
    font-family: "Montserrat", sans-serif;
    font-weight: 700;
    fill: var(--yellow);
  }
  .headline {
    font-family: "Anton", sans-serif;
    fill: var(--yellow);
  }
</style>
</head>
<body>
<main class="canvas">
  <section class="wrap-band">
    <div class="athlete-photo" role="img" aria-label="Black and white photo of a woman training on a cable pulldown in a gym"></div>

    <svg class="artwork" viewBox="0 0 1200 969" xmlns="http://www.w3.org/2000/svg">
      <!-- corner crosses -->
      <g class="corner-crosses" stroke="var(--white)" stroke-width="11">
        <line x1="980" y1="33" x2="1022" y2="80"/><line x1="1022" y1="33" x2="980" y2="80"/>
        <line x1="1058" y1="33" x2="1100" y2="80"/><line x1="1100" y1="33" x2="1058" y2="80"/>
        <line x1="1136" y1="33" x2="1178" y2="80"/><line x1="1178" y1="33" x2="1136" y2="80"/>
      </g>

      <!-- brand name -->
      <text class="brand-name" x="40" y="630" font-size="330" textLength="1106" lengthAdjust="spacingAndGlyphs">VolaRenx</text>

      <!-- tagline -->
      <text class="tagline" x="230" y="704" font-size="34" textLength="742" lengthAdjust="spacing">PERSONAL GROUP TRAINING</text>

      <!-- headline -->
      <text class="headline" x="283" y="882" font-size="160" textLength="878" lengthAdjust="spacingAndGlyphs">CHANGE BEGINS HERE</text>

      <!-- curly arrow toward the door -->
      <g class="curl-arrow" fill="none" stroke="var(--white)" stroke-width="7" stroke-linecap="round">
        <path d="M272 804 C240 835 210 868 190 858 C168 846 178 812 200 815 C222 818 220 860 190 880 C160 900 110 900 60 890"/>
      </g>
      <path d="M38 887 L82 860 L74 886 L82 908 Z" fill="var(--white)"/>

      <!-- hatched stripes -->
      <g class="hatch" stroke="var(--white)" stroke-width="4" fill="none">
        <path d="M0 969 L0 925 L304 925 L274 969"/>
        <line x1="20" y1="969" x2="40" y2="925"/>
        <line x1="40" y1="969" x2="60" y2="925"/>
        <line x1="60" y1="969" x2="80" y2="925"/>
        <line x1="80" y1="969" x2="100" y2="925"/>
        <line x1="100" y1="969" x2="120" y2="925"/>
        <line x1="120" y1="969" x2="140" y2="925"/>
        <line x1="140" y1="969" x2="160" y2="925"/>
        <line x1="160" y1="969" x2="180" y2="925"/>
        <line x1="180" y1="969" x2="200" y2="925"/>
        <line x1="200" y1="969" x2="220" y2="925"/>
        <line x1="220" y1="969" x2="240" y2="925"/>
        <line x1="240" y1="969" x2="260" y2="925"/>
        <line x1="260" y1="969" x2="280" y2="925"/>
      </g>
    </svg>
  </section>
</main>
</body>
</html>
```